We need UI/UX design for a public, informational website for The Copper Lantern.
The pages, structure, and content scope are already defined. Designers are required to work only on the UI/UX layout of these existing pages, focusing on clarity, hierarchy, spacing, and usability. Do not add, remove, rename, or reinterpret pages or content.
The website is strictly informational only. It must not include accounts, onboarding, payments, custody, escrow administration, marketplaces, dashboards, or any transactional functionality.
Scope of work
Apply UI/UX design to the predefined website pages
Design layout for text, images, notices, and sections
Ensure consistent components and layout patterns across page types
Optimize layouts for long form, compliance focused content
Content writing, page creation, and branding changes are out of scope.
Structure reference
The complete page list, hierarchy, and content definitions are provided in the technical documentation and must be treated as the primary source of truth.
A Figma link is provided only as a light visual reference for page existence and structure:
https://maple-kettle-48203917.plansite.example/
Designers must rely on the documentation for in depth and authoritative reference.
Brand guidelines
The Copper Lantern has existing brand guidelines and official logos, including light and dark versions. These assets will be provided and must be followed exactly. Designers must not redesign, alter, or reinterpret the brand identity.
Look and feel direction
The desired visual direction is inspired by:
https://quorvanta.example/
This reference is provided only to indicate:
Institutional and enterprise tone
Clean, modern typography
Strong hierarchy and generous whitespace
Editorial, content first layouts
Do not copy branding, layouts, components, or assets from the reference site.
Hero section direction
The hero section should follow a similar structural approach to the hero used on https://quorvanta.example/
, meaning:
Strong editorial framing
Clear headline hierarchy
Calm, institutional first impression
However, the background video must be Abu Dhabi focused, not generic or global. The video should visually reflect:
Abu Dhabi skyline or architectural language
Institutional, sovereign, long term infrastructure tone
Clean, slow, cinematic motion
No promotional, marketing, or lifestyle visuals
The hero must remain informational, restrained, and credible. No hype. No calls to invest. No implied participation.
Constraints
One global primary CTA only: “Continue to Brightmoor” (external)
All other interactions must be informational
No visuals or language implying offers, investment, eligibility, or participation
Clear separation between informational content and any external operational platforms
Deliverables
High fidelity UI/UX designs created in Figma, covering:
Desktop layouts
Tablet layouts where relevant
Mobile layouts
Complete Figma file(s) including:
All designed pages defined in the technical documentation
A reusable component library (headers, footers, cards, notice panels, forms, CTAs, typography styles, spacing system)
Clearly defined layout grids, spacing rules, and text styles
Proper use of components and variants, not detached frames
Designs prepared for developer handoff, including:
Clear layer naming and structure
Auto layout where appropriate
Consistent use of styles and components
Responsive behavior demonstrated within Figma
Notes or annotations only where necessary for clarity
No prototypes, interactions, or motion design beyond basic layout states, unless explicitly requested. The focus is static UI/UX clarity, not animation.
A detailed technical specification document and official brand assets will be provided.
Any designs delivered outside Figma, that alter structure or content, or that ignore the defined constraints, boundaries, or tone will be rejected.

```html
<!DOCTYPE html>
<html lang="en">
<head>
<meta charset="utf-8">
<title>The Copper Lantern</title>
<link rel="stylesheet" href="https://fonts.googleapis.com/css2?family=Space+Grotesk:wght@400;500;600;700&family=Poppins:wght@300;400;500&display=swap">
<style>
:root{
  --ink:#111111;
  --text:#2b2b2b;
  --white:#ffffff;
  --cyan:#22d3ee;
  --blue:#3d9bff;
  --violet:#9a5cf6;
  --footer:#1f1f1f;
  --muted:#bdbdbd;
  --band:linear-gradient(90deg,var(--blue) 0%,#6f7ffb 55%,var(--violet) 100%);
  --head:"Space Grotesk",sans-serif;
  --body:"Poppins",sans-serif;
}
*{margin:0;padding:0;box-sizing:border-box}
html,body{width:1200px;height:4598px;overflow:hidden}
body{position:relative;background:var(--white);font-family:var(--body);color:var(--text)}
.abs{position:absolute}
p{font-size:14.5px;line-height:25.5px}

/* header / hero */
.hero{left:0;top:0;width:1200px;height:721px;background:linear-gradient(180deg,#4a3a46 0%,#a05a3c 18%,#3c3f49 42%,#232a2e 70%,#2e3830 100%)}
.brand{display:flex;align-items:center;gap:12px;font-family:var(--head);font-weight:500;color:var(--white);letter-spacing:.5px}
.brand-dot{width:18px;height:18px;border-radius:50%;background:var(--cyan)}
.site-brand{left:75px;top:66px;font-size:21px}
.nav{left:358px;top:72px;display:flex;gap:0;font-family:var(--head);font-weight:600;font-size:13px;color:var(--white);letter-spacing:.4px}
.nav a{color:inherit;text-decoration:none;position:absolute;white-space:nowrap}
.nav a.active{color:var(--cyan);border-bottom:2px solid var(--cyan);padding-bottom:2px}
.hero-title{left:73px;top:296px;font-family:var(--head);font-weight:700;font-size:66px;color:var(--white);letter-spacing:.5px;line-height:1}
.hero-text{left:77px;top:378px;width:640px;color:var(--white);font-family:var(--head);font-size:17.5px;line-height:24px}
.btn{display:flex;align-items:center;justify-content:center;font-family:var(--head);font-weight:500;font-size:15px;text-decoration:none}
.btn-primary{left:75px;top:475px;width:221px;height:53px;background:#0f0f0f;color:var(--white)}
.btn-secondary{left:311px;top:475px;width:221px;height:53px;background:var(--cyan);color:#12315a}

/* generic */
.photo{border-radius:8px}
.sec-title{font-family:var(--head);font-weight:500;font-size:35px;line-height:40px;color:var(--ink)}
.band{left:0;width:1200px;background:var(--band)}
.band .sec-title,.band p{color:var(--white)}
.round{border-radius:50%;border:8px solid var(--white);background:linear-gradient(140deg,#b6bcc4,#5d6670 60%,#2d3238)}

/* ecosystem */
.eco-band{top:2258px;height:375px}
.eco-title{left:0;width:1200px;top:2308px;text-align:center;font-family:var(--head);font-weight:500;font-size:35px;color:var(--white)}
.eco-sub{left:0;width:1200px;top:2370px;text-align:center;font-size:14px;color:var(--white)}
.layer{width:322px;height:322px;border-radius:50%;background:var(--white);border:6px solid var(--violet);text-align:center;padding:0 34px}
.layer svg{display:block;margin:46px auto 0}
.layer h3{font-family:var(--head);font-weight:500;font-size:23px;color:var(--ink);margin-top:14px}
.layer p{font-size:14px;line-height:24px;margin-top:6px;color:#333}
.badge{width:52px;height:52px;border-radius:50%;background:var(--cyan);border:5px solid var(--white);font-family:var(--head);font-weight:700;font-size:24px;color:#0d1a2a;display:flex;align-items:center;justify-content:center}
.eco-note{left:100px;width:1000px;top:2775px;text-align:center;font-style:italic;font-size:14.5px;line-height:26px;color:#222}

/* contact */
.contact-band{top:3899px;height:348px;background:linear-gradient(90deg,#22d3ee 0%,#5e97fb 55%,var(--violet) 100%)}
.contact-title{left:0;width:1200px;top:3962px;text-align:center;font-family:var(--head);font-weight:500;font-size:35px;color:var(--white)}
.contact-text{left:160px;width:880px;top:4024px;text-align:center;color:var(--white);font-size:14.5px;line-height:26px}
.btn-contact{left:489px;top:4126px;width:222px;height:53px;background:#0f0f0f;color:var(--white);font-size:16px}

/* footer */
.footer{left:0;top:4247px;width:1200px;height:351px;background:var(--footer);color:var(--white)}
.foot-brand{left:75px;top:4342px;font-size:26px}
.copy{left:75px;top:4428px;font-size:12px;line-height:22px;color:#d8d8d8}
.foot-head{font-family:var(--head);font-weight:600;font-size:19px;color:var(--white);letter-spacing:.4px}
.foot-link{font-size:14.5px;color:#e6e6e6}
.social{left:795px;top:4473px;display:flex;gap:22px}
.social span{width:20px;height:20px;border-radius:50%;background:var(--white)}
.notice-label{left:75px;top:4523px;font-size:12px;font-weight:500;color:var(--cyan)}
.notice-text{left:75px;top:4546px;font-size:11.5px;color:#9a9a9a}
</style>
</head>
<body>

<header>
  <div class="abs hero" role="img" aria-label="Abu Dhabi skyline at dusk with towers over the waterfront"></div>
  <div class="abs brand site-brand"><span class="brand-dot"></span>The Copper Lantern</div>
  <nav class="abs nav">
    <a class="active" style="left:0">HOME</a>
    <a style="left:90px">FRAMEWORK</a>
    <a style="left:228px">PROJECTS</a>
    <a style="left:350px">BRIGHTMOOR</a>
    <a style="left:478px">INSIGHTS</a>
    <a style="left:598px">COMPANY</a>
    <a style="left:703px">CONTACT</a>
  </nav>
  <h1 class="abs hero-title">THE COPPER LANTERN</h1>
  <p class="abs hero-text">Duis mollis, est non commodo luctus, nisi erat porttitor ligula, eget lacinia odio sem nec elit. Morbi leo risus, porta ac consectetur ac, vestibu lum at eros. Nulla vitae elit libero.</p>
  <a class="abs btn btn-primary">CONTINUE TO BRIGHTMOOR</a>
  <a class="abs btn btn-secondary">LEARN THE FRAMEWORK</a>
</header>

<main>
  <section>
    <div class="abs photo" style="left:75px;top:789px;width:512px;height:386px;background:linear-gradient(135deg,#4aa79c,#c9c2b4 45%,#6a6e5e)" role="img" aria-label="Team meeting around a laptop in a bright office"></div>
    <h2 class="abs sec-title" style="left:616px;top:804px">The Copper Lantern</h2>
    <p class="abs" style="left:616px;top:858px;width:520px">The Copper Lantern is a governance and project origination group. Its purpose is to define structural standards and oversight principles for complex initiatives that may involve multiple parties, staged execution, and long-term accountability. This website publishes those standards and explains how responsibilities are separated across governance, operations, and project-level execution.</p>
    <p class="abs" style="left:616px;top:1024px;width:520px">This site is informational. It does not provide onboarding, account access, eligibility checks, custody of funds, escrow administration, or transaction execution. Where operational workflows exist, they are provided through a separate operating platform under separate terms and policies.</p>
  </section>

  <section>
    <div class="abs band" style="top:1303px;height:375px"></div>
    <h2 class="abs sec-title" style="left:75px;top:1352px;width:560px">Governance and Project Origination</h2>
    <p class="abs" style="left:75px;top:1446px;width:540px">Governance in this context refers to the standards that determine how projects are structured and how oversight is described. Origination refers to the initial design and definition of an initiative, including role separation, reporting expectations, and boundary setting before execution begins. The Copper Lantern focuses on these governance-level elements rather than on operating day-to-day workflows.</p>
    <div class="abs round" style="left:648px;top:1260px;width:478px;height:478px" role="img" aria-label="Colleagues reviewing architectural plans and laptops around a table"></div>
  </section>

  <section>
    <div class="abs photo" style="left:75px;top:1790px;width:512px;height:386px;background:linear-gradient(135deg,#d9dcdb,#9aa19c 50%,#4b4f4a)" role="img" aria-label="Group workshop in front of a whiteboard"></div>
    <h2 class="abs sec-title" style="left:616px;top:1835px">Clear Role Separation</h2>
    <p class="abs" style="left:616px;top:1889px;width:520px">The ecosystem is designed around clear separation of responsibilities. Governance activities belong at the framework layer. Operational workflows, where available, belong on a separate operating platform designed for process execution and recordkeeping. Assets and project execution, where applicable, belong at the project level through ring-fenced structures created for specific initiatives. This separation is intended to reduce ambiguity and help stakeholders understand who is responsible for what.</p>
  </section>

  <section>
    <div class="abs band eco-band"></div>
    <h2 class="abs eco-title">How the Ecosystem Works</h2>
    <p class="abs eco-sub">At a high level, the ecosystem can be understood as three layers</p>

    <div class="abs layer" style="left:76px;top:2422px">
      <svg width="54" height="48" viewBox="0 0 54 48" fill="none" stroke="#8a7df2" stroke-width="2"><path d="M4 14 27 3l23 11z"/><path d="M6 18h42M10 18v22M19 18v22M27 18v22M35 18v22M44 18v22M4 42h46M2 46h50"/></svg>
      <h3>Governance</h3>
      <p>Defines standards, explains role boundaries, and publishes framework information.</p>
    </div>
    <div class="abs layer" style="left:438px;top:2422px">
      <svg width="70" height="54" viewBox="0 0 70 54" fill="none" stroke="#6f8ff2" stroke-width="2"><circle cx="22" cy="30" r="14"/><circle cx="22" cy="30" r="5"/><circle cx="50" cy="16" r="10"/><circle cx="50" cy="16" r="3.5"/><circle cx="52" cy="42" r="8"/><circle cx="52" cy="42" r="2.5"/><path d="M22 12v-4M22 52v-4M4 30H0M44 30h-4M9 17l-3-3M35 43l3 3M9 43l-3 3M35 17l3-3"/></svg>
      <h3 style="margin-top:8px">Operations</h3>
      <p>Manages workflow processes such as documentation steps and record-anchored audit events through a separate platform.</p>
    </div>
    <div class="abs layer" style="left:802px;top:2422px">
      <svg width="64" height="52" viewBox="0 0 64 52" fill="none" stroke="#8a7df2" stroke-width="2"><rect x="10" y="4" width="44" height="32" rx="2"/><rect x="14" y="8" width="36" height="24"/><path d="M2 44h60l-4-8H6z"/></svg>
      <h3>Project Execution</h3>
      <p>Occurs at the project level through dedicated structures that hold responsibilities and assets where applicable.</p>
    </div>
    <div class="abs badge" style="left:103px;top:2439px">1</div>
    <div class="abs badge" style="left:465px;top:2676px">2</div>
    <div class="abs badge" style="left:1044px;top:2439px">3</div>

    <p class="abs eco-note">This website focuses on the governance layer and provides links to learn about structural concepts such as role separation, escrow and milestone framing, and recordkeeping terminology.</p>
  </section>

  <section>
    <div class="abs band" style="top:2952px;height:373px"></div>
    <h2 class="abs sec-title" style="left:75px;top:3009px;width:560px">Independent Escrow and Milestone Oversight</h2>
    <p class="abs" style="left:75px;top:3102px;width:545px">Some initiatives use independent escrow arrangements to coordinate staged releases linked to milestone completion. Escrow can support execution discipline by requiring defined evidence before releases occur. Escrow does not guarantee outcomes, timelines, or success, and it is not administered by this website operator. This site describes the concept for clarity and transparency.</p>
    <div class="abs round" style="left:648px;top:2900px;width:478px;height:478px;background:linear-gradient(140deg,#1c2e4a,#0e1a2e 55%,#3a2440)" role="img" aria-label="Hand touching a digital milestone path leading to a target"></div>
  </section>

  <section>
    <div class="abs photo" style="left:75px;top:3438px;width:512px;height:386px;background:linear-gradient(135deg,#1f3f49,#2b5661 50%,#8a7a6c)" role="img" aria-label="Hands on a keyboard with floating document approval graphics"></div>
    <h2 class="abs sec-title" style="left:616px;top:3514px;width:420px">Where Operational Workflows Happen</h2>
    <p class="abs" style="left:616px;top:3610px;width:520px">Operational workflows, including any onboarding or workflow participation where permitted, occur on a separate operating platform under separate terms and policies. If you need operational access, use the Brightmoor page on this site to navigate externally. This website does not host those workflows.</p>
  </section>

  <section>
    <div class="abs contact-band" style="left:0;width:1200px"></div>
    <h2 class="abs contact-title">Contact and Inquiries</h2>
    <p class="abs contact-text">If you have questions about governance framework concepts, role boundaries, or information published on this website, you can contact the team using the Contact page. Do not submit sensitive personal data through public forms.</p>
    <a class="abs btn btn-contact">Contact the Team</a>
  </section>
</main>

<footer>
  <div class="abs footer"></div>
  <div class="abs brand foot-brand"><span class="brand-dot"></span>The Copper Lantern</div>
  <p class="abs copy">© Copyright © 2026 The Copper Lantern.<br>All Right Reserved</p>

  <h4 class="abs foot-head" style="left:436px;top:4296px">QUICK LINKS</h4>
  <span class="abs foot-link" style="left:436px;top:4335px">Framework</span>
  <span class="abs foot-link" style="left:436px;top:4369px">Projects</span>
  <span class="abs foot-link" style="left:436px;top:4403px">Brightmoor</span>
  <span class="abs foot-link" style="left:436px;top:4437px">Insights</span>
  <span class="abs foot-link" style="left:588px;top:4335px">Company</span>
  <span class="abs foot-link" style="left:588px;top:4369px">Contact</span>
  <span class="abs foot-link" style="left:588px;top:4403px">Legal</span>
  <span class="abs foot-link" style="left:588px;top:4437px">Glossary</span>

  <h4 class="abs foot-head" style="left:795px;top:4296px">CONTACT INFO</h4>
  <p class="abs foot-link" style="left:795px;top:4330px;font-size:14px;line-height:26px">48 Harlow Lane Suite 12,<br>Northfield 20451, United States</p>
  <span class="abs foot-link" style="left:795px;top:4395px">+1-555-014-2290</span>
  <span class="abs foot-link" style="left:795px;top:4429px">hello@copperlantern.example</span>
  <div class="abs social" aria-label="Social channels"><span></span><span></span><span></span><span></span><span></span></div>

  <span class="abs notice-label">Informational notice:</span>
  <span class="abs notice-text">This website is provided for general informational purposes only. Nothing on this site is an offer, solicitation, or professional advice</span>
</footer>

</body>
</html>
```